Juice up my new website for book profits on Orbimart

I have a website that needs a new look. I made a video of the past and in progress website: http://vexaclip.net/tq8mzR2KWD.... here is the site in progress. http://brew.corestretchguide.net/...this will be a WordPress website......https://pagevault.example/snap/20180305134456/http://www.pressing-tips.net/

This website is setup to primary sell on Orbimart.

eBook: https://www.orbimart.example/Nectar-Blend-Formulas-For-Vigor-ebook/dp/K7RQPWZ2XN/ref=sr_1_4?dchild=1&keywords=Nectar+and+Blend+formulas+for+vigor&qid=1634055930&s=books&sr=1-4

Target Market(s)

Health and weight conscience people

Industry/Entity Type

Health

Number of Pages Required

2 page

Font styles to use
Serif

Requirements
Must have
• slider, sign up form, buy the ebook or hardcopy book.
Nice to have
• happy people drinking juice
Should not have
• Sidebar

```html
<!DOCTYPE html>
<html lang="en">
<head>
<meta charset="utf-8">
<title>Pressing Tips – Nectar and Blend Formulas for Vigor</title>
<link rel="stylesheet" href="https://fonts.googleapis.com/css2?family=Oswald:wght@300;400;500&family=Roboto:wght@400;500;700&family=Lora:ital@1&display=swap">
<style>
:root{
  --purple:#8e3a80;
  --orange:#f28a1e;
  --teal:#3a9b9b;
  --ink:#1b1b1b;
  --body:#444;
  --rule:#cfcfcf;
  --footer:#121212;
  --faq-bg:#f2f2f0;
}
*{box-sizing:border-box;margin:0;padding:0}
html,body{width:1200px;height:4247px;overflow:hidden}
body{font-family:"Roboto",sans-serif;color:var(--ink);background:#fff;position:relative}
section,header,footer{position:absolute;left:0;width:1200px;overflow:hidden}
.abs{position:absolute}
.display{font-family:"Oswald",sans-serif;text-transform:uppercase;font-weight:500;letter-spacing:.2px}
.pill{position:absolute;display:flex;align-items:center;justify-content:center;border-radius:22px;font-family:"Roboto",sans-serif;font-weight:500;font-size:15px;color:#fff}

/* header */
.site-header{top:0;height:72px;background:#fff}
.brand{left:110px;top:16px}
.brand-name{font-family:"Oswald",sans-serif;font-weight:500;font-size:27px;color:var(--ink);letter-spacing:.5px;text-transform:uppercase}
.nav a{position:absolute;top:27px;font-family:"Roboto",sans-serif;font-weight:500;font-size:14px;color:var(--ink);text-decoration:none;letter-spacing:.3px}

/* hero */
.hero{top:72px;height:627px;background:linear-gradient(100deg,#e8e2d8 0%,#ddd3c4 38%,#f0a23a 58%,#e9532b 72%,#c8182b 84%,#f39a1d 100%)}
.hero-title{left:110px;top:132px;font-size:50px;line-height:56px;color:var(--ink)}
.hero-text{left:111px;top:258px;width:480px;font-family:"Oswald",sans-serif;font-weight:300;font-size:19px;line-height:31px;color:var(--ink);white-space:nowrap}
.hero .pill{top:366px;height:40px;width:152px;background:var(--purple)}
.dots{display:flex;gap:8px}
.dot{width:11px;height:11px;border-radius:50%;border:1.5px solid #fff}
.dot.on{background:#fff}

/* about */
.about{top:699px;height:606px;background:#fff}
.about-frame{left:112px;top:87px;width:445px;height:415px;border:3px solid var(--purple);border-radius:6px}
.about-photo{left:130px;top:104px;width:444px;height:415px;border-radius:6px;background:linear-gradient(160deg,#eef0f1,#cdd3d6 55%,#8a7a6a)}
.about h2{left:651px;top:96px;font-size:50px;color:var(--ink)}
.about-copy{left:651px;top:170px;width:425px;font-size:13.5px;line-height:25.6px;color:var(--body)}
.about-copy p+p{margin-top:9px}
.about .pill{left:651px;top:461px;width:152px;height:40px;background:var(--purple)}

/* reading */
.reading{top:1305px;height:613px;background:radial-gradient(circle at 20% 30%,#f7a23c,transparent 40%),radial-gradient(circle at 85% 70%,#f9b04e,transparent 40%),var(--orange)}
.reading h2{left:0;width:1200px;top:68px;text-align:center;font-size:41px;color:#fff}
.arch{top:236px;width:348px;height:377px;background:var(--purple);border-radius:174px 174px 0 0}
.book{top:150px;width:231px;height:367px;background:linear-gradient(135deg,#b61e2b,#8c1320 70%,#5a0d15);box-shadow:6px 6px 14px rgba(0,0,0,.35)}
.reading .pill{top:547px;width:151px;height:40px;background:var(--orange)}

/* articles */
.articles{top:1918px;height:787px;background:#fff}
.articles h2{left:0;width:1200px;top:72px;text-align:center;font-size:41px}
.feature-img{left:129px;top:160px;width:476px;height:277px;background:linear-gradient(120deg,#3d6b1e,#7fae2c 30%,#e0541f 55%,#6e2a3d 80%,#3a3a2a)}
.date{font-family:"Oswald",sans-serif;font-weight:300;font-size:13px;color:var(--teal)}
.post-title{font-family:"Oswald",sans-serif;font-weight:500;font-size:21px;line-height:24px;color:var(--ink)}
.more{font-family:"Roboto",sans-serif;font-weight:500;font-size:15px;color:var(--purple);letter-spacing:.4px}
.excerpt{left:129px;top:540px;width:455px;font-size:13.5px;line-height:29px;color:var(--body)}
.thumb{left:630px;width:148px;height:150px}
.divider{left:634px;width:439px;height:1px;background:var(--rule)}

/* testimonials */
.testimonials{top:2705px;height:408px;background:var(--purple)}
.testimonials h2{left:651px;top:58px;font-size:44px;color:#fff}
.t-rule{left:651px;top:120px;width:437px;height:1px;background:rgba(255,255,255,.6)}
.quote{left:672px;top:152px;width:425px;font-family:"Lora",serif;font-style:italic;font-size:19.5px;line-height:30px;color:#fff}
.qmark{font-family:"Oswald",sans-serif;font-size:34px;color:#fff;line-height:1}

/* faq */
.faq{top:3113px;height:458px;background:var(--faq-bg)}
.faq-img{left:560px;top:0;width:640px;height:458px;background:linear-gradient(110deg,#f2f2f0 0%,#e8ecd9 30%,#8fbf3c 55%,#3b8a24 70%,#f4d03c 88%,#e0e4dc 100%)}
.faq h2{left:124px;top:104px;font-size:40px}
.faq-item{left:119px;width:438px;height:43px;background:#fff;border-radius:22px;display:flex;align-items:center;justify-content:space-between;padding:0 26px 0 34px;font-family:"Oswald",sans-serif;font-size:16px;text-transform:uppercase;color:var(--ink)}
.faq-item svg{width:20px;height:20px}

/* signup */
.signup{top:3571px;height:364px;background:radial-gradient(circle at 15% 70%,#f79a2a,transparent 40%),radial-gradient(circle at 85% 30%,#f5a045,transparent 45%),var(--orange)}
.signup h2{left:0;width:1200px;top:64px;text-align:center;font-size:28px;line-height:39px;color:#fff;font-weight:400}
.field{top:171px;width:298px;height:43px;background:#fff;border-radius:22px;display:flex;align-items:center;padding-left:24px;font-size:13px;color:#777}
.signup .pill{left:488px;top:243px;width:222px;height:43px;border:2px solid #fff;background:transparent;font-size:14px}

/* footer */
.site-footer{top:3935px;height:312px;background:var(--footer);color:#fff}
.site-footer h2{left:0;width:1200px;top:68px;text-align:center;font-size:36px;color:#fff}
.foot-nav a{position:absolute;top:143px;font-size:14px;font-weight:500;color:#fff;text-decoration:none;letter-spacing:.3px}
.social{top:202px;left:492px;display:flex;gap:10px}
.social span{width:34px;height:34px;border-radius:50%;background:#2a2a2a;border:1px solid #3a3a3a}
.copy{left:0;width:1200px;top:271px;text-align:center;font-size:14px;color:#ddd}
</style>
</head>
<body>

<header class="site-header">
  <div class="abs brand"><span class="brand-name">Pressing Tips</span></div>
  <nav class="nav">
    <a style="left:456px" href="#">FREE LESSONS</a>
    <a style="left:613px" href="#">THE DIFFERENCE</a>
    <a style="left:791px" href="#">ARTICLES</a>
    <a style="left:911px" href="#">CONTACT</a>
    <a style="left:1027px" href="#">PRAISE</a>
  </nav>
</header>

<section class="hero" role="img" aria-label="Fresh juices and smoothies in glasses with oranges, grapefruit, tomato, kiwi and berries">
  <svg class="abs" style="left:60px;top:250px" width="24" height="46" viewBox="0 0 24 46"><path d="M22 2 2 23l20 21" fill="none" stroke="#222" stroke-width="2"/></svg>
  <svg class="abs" style="left:1103px;top:250px" width="24" height="46" viewBox="0 0 24 46"><path d="M2 2l20 21L2 44" fill="none" stroke="#fff" stroke-width="2"/></svg>
  <h1 class="abs display hero-title">Nectar and Blend<br>Formulas for Vigor</h1>
  <p class="abs hero-text">Discover the Power of Fresh Fruits and Vegetables with Easy and<br>Delicious Juice and Smoothie Recipes Based on Exciting New<br>Research!</p>
  <a class="pill" style="left:113px">Free Lessons</a>
  <a class="pill" style="left:277px">Pressing Tips</a>
  <div class="abs dots" style="left:563px;top:589px"><span class="dot"></span><span class="dot on"></span><span class="dot"></span><span class="dot"></span></div>
</section>

<section class="about">
  <div class="abs about-frame"></div>
  <div class="abs about-photo" role="img" aria-label="Smiling woman holding a glass of red juice in a bright kitchen"></div>
  <h2 class="abs display">About Us</h2>
  <div class="abs about-copy">
    <p>We began this site in 2011 to share our joy and experience with juicing and blending, particularly little-known 'secrets' that save you time and money. In 2014 one of our principle authors, Ned Calloway. was chosen by Howwise to be their 'Juicing Expert' a position he held for 2 years. Ned creates a fresh juice or smoothie every day with recipes that help keep his wife's breast cancer in remission.</p>
    <p>The mission of our site is to provide the most up-to-date information about juicing and smoothies, because the benefits are astounding and not well understood,</p>
  </div>
  <a class="pill">Learn More</a>
</section>

<section class="reading">
  <h2 class="abs display">Recommended Reading!</h2>
  <div class="abs arch" style="left:165px"></div>
  <div class="abs arch" style="left:601px"></div>
  <div class="abs book" style="left:239px" role="img" aria-label="Book cover: Nectar and Blend Formulas for Vigor, ebook edition"></div>
  <div class="abs book" style="left:675px" role="img" aria-label="Book cover: Nectar and Blend Formulas for Vigor, hardcopy edition"></div>
  <a class="pill" style="left:264px">ebook</a>
  <a class="pill" style="left:699px">Hardcopy</a>
</section>

<section class="articles">
  <h2 class="abs display">Most Popular Articles</h2>
  <div class="abs feature-img" role="img" aria-label="Assorted fresh vegetables and fruits"></div>
  <div class="abs date" style="left:129px;top:460px">March 5, 2015 by Ned Calloway</div>
  <div class="abs post-title" style="left:129px;top:498px">Recipes for Better Sex!</div>
  <p class="abs excerpt">There Are Certain Compounds In Fresh Fruits &amp; Vegetables Proven To Enhance Sexual Performance! Many changes occur in the body which directly affect our sex drive, performance and pleasure as part of the natural aging process. Both women and men</p>
  <div class="abs more" style="left:129px;top:674px">Continue Reading...</div>

  <div class="abs thumb" style="top:160px;background:linear-gradient(#4e9a2a,#8cc63f 70%,#e8e8e8)" role="img" aria-label="Wheatgrass growing in a white tray"></div>
  <div class="abs date" style="left:809px;top:188px">March 5, 2015 by Ned Calloway</div>
  <div class="abs post-title" style="left:809px;top:221px">Grow Your Own Wheatgrass</div>
  <div class="abs more" style="left:809px;top:266px">Continue Reading...</div>
  <div class="abs divider" style="top:332px"></div>

  <div class="abs thumb" style="top:354px;background:linear-gradient(135deg,#3a3f55,#1c1f2e 60%,#4a4e63)" role="img" aria-label="Pile of fresh blackberries"></div>
  <div class="abs date" style="left:809px;top:381px">March 5, 2015 by Ned Calloway</div>
  <div class="abs post-title" style="left:809px;top:413px">Greens In Your Own Back<br>Yard!</div>
  <div class="abs more" style="left:809px;top:475px">Continue Reading...</div>
  <div class="abs divider" style="top:526px"></div>

  <div class="abs thumb" style="top:546px;background:linear-gradient(135deg,#e8e2d8,#b81c2a 50%,#7a1018)" role="img" aria-label="Fresh cherries in a cloth bag"></div>
  <div class="abs date" style="left:809px;top:574px">March 5, 2015 by Ned Calloway</div>
  <div class="abs post-title" style="left:809px;top:607px">How To Avoid the Dangers</div>
  <div class="abs more" style="left:809px;top:649px">Continue Reading...</div>
</section>

<section class="testimonials">
  <svg class="abs" style="left:0;top:0" width="620" height="408" viewBox="0 0 620 408" role="img" aria-label="Colourful smoothies in glass bottles with striped straws and fruit">
    <defs><linearGradient id="smoothieTones" x1="0" x2="1" y1="0" y2="0"><stop offset="0" stop-color="#f2c53a"/><stop offset=".3" stop-color="#f1a7b8"/><stop offset=".55" stop-color="#9a3f8a"/><stop offset=".75" stop-color="#f08a2a"/><stop offset="1" stop-color="#a9c95a"/></linearGradient></defs>
    <path d="M0 0H503C580 90 640 230 520 408H0Z" fill="url(#smoothieTones)"/>
  </svg>
  <h2 class="abs display">Testimonials</h2>
  <div class="abs t-rule"></div>
  <span class="abs qmark" style="left:645px;top:156px">“</span>
  <p class="abs quote">“If you're looking for a refreshing way to eat more veggies and fruits, try these great recipes that save you time &amp; lose weight. Your body will thank you for it. Great recipes... Keep up the nice work.”&nbsp;<span class="qmark" style="font-style:normal;font-size:30px;vertical-align:-10px">”</span></p>
  <div class="abs dots" style="left:676px;top:329px;gap:5px"><span class="dot" style="border-color:#ddd"></span><span class="dot" style="border-color:#ddd"></span><span class="dot on"></span><span class="dot" style="border-color:#ddd"></span><span class="dot" style="border-color:#ddd"></span></div>
</section>

<section class="faq">
  <div class="abs faq-img" role="img" aria-label="Green juice in a jar with a straw, bananas, apple, lemon and spinach"></div>
  <h2 class="abs display">Frequently Asked Questions</h2>
  <div class="abs faq-item" style="top:179px">Avoiding Dangers<svg viewBox="0 0 20 20"><path d="M10 1v18M1 10h18" stroke="#333" stroke-width="1.6"/></svg></div>
  <div class="abs faq-item" style="top:239px">Juicing on a Budget<svg viewBox="0 0 20 20"><path d="M10 1v18M1 10h18" stroke="#333" stroke-width="1.6"/></svg></div>
  <div class="abs faq-item" style="top:299px">Why Are Greens So Important<svg viewBox="0 0 20 20"><path d="M10 1v18M1 10h18" stroke="#333" stroke-width="1.6"/></svg></div>
</section>

<section class="signup">
  <h2 class="abs display">Sign Up for All the Best &amp; Latest Tips &amp; Tricks for the Most<br>Delicious &amp; Nutritious Fresh Juice or Smoothie!</h2>
  <div class="abs field" style="left:292px">Your Name</div>
  <div class="abs field" style="left:608px">Your email address</div>
  <a class="pill">Get My Free Course</a>
</section>

<footer class="site-footer">
  <h2 class="abs display">Pressing Tips</h2>
  <nav class="foot-nav">
    <a style="left:222px" href="#">HOME</a>
    <a style="left:318px" href="#">FREE LESSONS</a>
    <a style="left:483px" href="#">THE DIFFERENCE</a>
    <a style="left:667px" href="#">ARTICLES</a>
    <a style="left:797px" href="#">CONTACT</a>
    <a style="left:919px" href="#">PRAISE</a>
  </nav>
  <div class="abs social"><span></span><span></span><span></span><span></span><span></span></div>
  <p class="abs copy">© 2020 Pressing Tips. All Rights Reserved.</p>
</footer>

</body>
</html>
```